Internet Of Things brochure

Need to create a brochure with a common theme to our website and the last 2 pages of the attached file. All the contect is in the file that I have attached.
website www.norvalenetworks.com.au

Industry/Entity Type

Internet

```html
<!DOCTYPE html>
<html lang="en">
<head>
<meta charset="utf-8">
<title>Smart Cities Initiative – Norvale Networks IoT Brochure</title>
<link rel="stylesheet" href="https://fonts.googleapis.com/css2?family=Open+Sans:wght@400;600;700&family=Libre+Baskerville:wght@700&display=swap">
<style>
:root{
  --bg:#3b3b3d;
  --navy:#0d3a6e;
  --navy-deep:#0a2a55;
  --blue-mid:#1a6fc0;
  --cyan:#1fdcf8;
  --ink:#0c2a57;
  --white:#ffffff;
  --sky:#3cc4ef;
  --pillar:#8fc8e6;
  --grey:#8ea2b6;
  --dark:#0b1f45;
}
*{box-sizing:border-box;margin:0;padding:0}
html,body{width:1200px;height:902px;overflow:hidden}
body{background:var(--bg);font-family:"Open Sans",Arial,sans-serif;color:var(--white);position:relative}
.page{position:absolute;top:87px;width:530px;height:742px;overflow:hidden;
  background:linear-gradient(180deg,var(--navy) 0%,var(--navy) 14%,var(--blue-mid) 42%,#19b6ea 68%,var(--cyan) 100%);
  box-shadow:0 6px 18px rgba(0,0,0,.45)}
.page--one{left:47px}
.page--two{left:630px}
.header{position:absolute;left:0;top:0;width:100%;height:87px;background:var(--navy-deep)}
.brands{position:absolute;left:30px;top:0;height:87px;display:flex;align-items:center;gap:18px}
.brand{font-weight:700;color:var(--white);white-space:nowrap}
.brand--main{font-size:15px;line-height:15px}
.brand--partner{font-size:11px;line-height:12px;text-transform:uppercase;font-weight:600}
.brand--cloud{font-size:15px;line-height:16px;font-weight:600}
.contact{position:absolute;right:16px;top:30px;font-size:9.5px;line-height:12px;text-align:right}
.title{position:absolute;left:22px;font-family:"Libre Baskerville",Georgia,serif;font-weight:700;font-size:19px;letter-spacing:.3px}
.copy{position:absolute;font-size:9.4px;line-height:12.4px}
.illustration{position:absolute;border-radius:4px;background:linear-gradient(180deg,rgba(255,255,255,.85),rgba(207,233,247,.55))}
.feature{position:absolute;width:150px}
.feature__head{font-weight:700;font-size:9.6px;text-transform:uppercase;height:22px;display:flex;align-items:center;gap:8px}
.feature__icon{width:26px;height:22px;border-radius:50%;background:rgba(255,255,255,.8);flex:none}
.feature__text{font-weight:600;font-size:8.8px;line-height:12.4px;color:var(--ink);margin-top:4px}
.pillar{position:absolute;top:213px;width:32px;height:213px;background:var(--pillar)}
.pillar span{position:absolute;left:50%;top:50%;transform:translate(-50%,-50%) rotate(-90deg);white-space:nowrap;font-size:8.5px}
.layer{position:absolute;left:138px;width:272px}
.layer__item{position:absolute;font-size:6.8px;line-height:8.5px;display:flex;align-items:center;gap:4px}
.dot{width:10px;height:10px;border-radius:50%;background:var(--white);flex:none}
.tag{position:absolute;left:410px;height:21px;padding-left:6px;font-size:9px;line-height:21px;width:108px}
.tag::after{content:"";position:absolute;right:-4px;top:4px;border-left:6px solid rgba(255,255,255,.6);border-top:6px solid transparent;border-bottom:6px solid transparent}
.subhead{position:absolute;left:22px;font-weight:700}
.commit{position:absolute;left:22px;top:583px;list-style:none;font-size:9.2px;line-height:12px;width:490px}
.commit li{display:flex;gap:8px;margin-bottom:9px}
.commit b{flex:none;width:12px;height:12px;border:1px solid var(--white);border-radius:50%;font-size:7.5px;line-height:10px;text-align:center;font-weight:600}
</style>
</head>
<body>

<section class="page page--one">
  <header class="header">
    <div class="brands">
      <div class="brand brand--main">Norvale<br>Networks</div>
      <div class="brand brand--partner">Corvan<br>Partner Business</div>
      <div class="brand brand--cloud">Altrix<br>Partner</div>
    </div>
    <div class="contact">P: 1300 555 019 A: 18 – 20 Calder<br>Road Merrowvale, NSW, 2199<br>W: norvalenetworks.com.au</div>
  </header>

  <h1 class="title" style="top:133px">SMART CITIES INITIATIVE</h1>
  <p class="copy" style="left:22px;top:178px;width:252px">A smart city is an urban development vision to integrate multiple information and communication technology (ICT) and Internet of things (IoT) solutions in a secure fashion to manage a city's assets – the city's assets include, but are not limited to, local departments' information systems, schools, libraries, transportation systems, hospitals, power plants, water supply networks, waste management, law enforcement, and other community services. The goal of building a smart city is to improve quality of life by using urban informatics and technology to improve the efficiency of services and meet residents' needs.</p>
  <div class="illustration" role="img" aria-label="White line illustration of a city skyline with wind turbines, a wireless signal, a billboard, traffic light and car" style="left:282px;top:168px;width:245px;height:122px"></div>

  <p class="copy" style="left:22px;top:352px;width:492px">ICT allows city officials to interact directly with the community and the city infrastructure and to monitor what is happening in the city, how the city is evolving, and how to enable a better quality of life. Through the use of sensors integrated with real-time monitoring systems, data are collected from citizens and devices – then processed and analyzed. The information and knowledge gathered are keys to tackling inefficiency. Norvale Networks has the ability and smarts to push these solutions forward.</p>
  <p class="copy" style="left:22px;top:428px;width:492px">Norvale Digital and Norvale Networks together with the partnership of Corvan and Altrix Nimbus Cloud hosting all these systems, solutions and devices have never been easier and cost effective to deploy and capitalize on.</p>

  <div class="feature" style="left:20px;top:518px">
    <div class="feature__head">Smart Governance <span class="feature__icon" role="img" aria-label="Speech bubble icon"></span></div>
    <p class="feature__text">Interconnected within-city and across-city governance, including ICT-enabled services and interactions between public and private sectors.</p>
  </div>
  <div class="feature" style="left:213px;top:518px">
    <div class="feature__head">Smart Economy <span class="feature__icon" role="img" aria-label="Globe with shopping cart icon"></span></div>
    <p class="feature__text">E-business and e-commerce, ICT-enabled manufacturing and delivery of services, as well as new products, new services and business models.</p>
  </div>
  <div class="feature" style="left:367px;top:518px">
    <div class="feature__head">Smart Mobility <span class="feature__icon" role="img" aria-label="Bicycle icon"></span></div>
    <p class="feature__text">ICT supported and integrated transport and logistics. Sustainable, safe and interconnected systems for public transport, cars, bicycles and pedestrians.</p>
  </div>
  <div class="feature" style="left:20px;top:642px">
    <div class="feature__head">Smart Environment <span class="feature__icon" role="img" aria-label="Tree icon"></span></div>
    <p class="feature__text">Smart energy including renewables, ICT-enabled energy grids, pollution control and monitoring, green buildings and green urban planning.</p>
  </div>
  <div class="feature" style="left:203px;top:642px">
    <div class="feature__head">Smart People <span class="feature__icon" role="img" aria-label="Light bulb icon"></span></div>
    <p class="feature__text">Those with e-skills, working in ICT-enabled roles, having access to education and training, human resources and capacity management.</p>
  </div>
  <div class="feature" style="left:373px;top:642px">
    <div class="feature__head">Smart Living <span class="feature__icon" role="img" aria-label="Wireless signal icon"></span></div>
    <p class="feature__text">ICT-enabled lifestyles, behaviour and consumption. Healthy and safe living in a culturally vibrant city with good quality housing.</p>
  </div>
</section>

<section class="page page--two">
  <header class="header">
    <div class="brands">
      <div class="brand brand--main">Norvale<br>Networks</div>
      <div class="brand brand--partner">Corvan<br>Partner Business</div>
      <div class="brand brand--cloud">Altrix<br>Partner</div>
    </div>
    <div class="contact">P: 1300 555 019 A: 18 – 20 Calder<br>Road Merrowvale, NSW, 2199<br>W: norvalenetworks.com.au</div>
  </header>

  <h1 class="title" style="top:116px">SMART CITIES INITIATIVE</h1>
  <div class="illustration" role="img" aria-label="Smart City line illustration with skyline, clouds, cyclist and car" style="left:136px;top:146px;width:266px;height:60px"></div>

  <div class="pillar" style="left:20px"><span>Services</span></div>
  <div class="pillar" style="left:60px"><span>IoT &amp; Cyber Security</span></div>
  <div class="pillar" style="left:100px"><span>Context-aware Service Management</span></div>

  <div class="layer" style="top:213px;height:72px;background:var(--sky)">
    <div style="position:absolute;left:28px;top:6px;font-size:11px">NEXUS platform</div>
    <div class="layer__item" style="left:20px;top:31px"><span class="dot"></span><b>Device management</b></div>
    <div class="layer__item" style="left:146px;top:31px"><span class="dot"></span><b>Data collection &amp; analytics</b></div>
    <div class="layer__item" style="left:20px;top:52px"><span class="dot"></span><b>Connectivity management</b></div>
    <div class="layer__item" style="left:146px;top:52px"><span class="dot"></span><b>Application enablement</b></div>
  </div>
  <div class="layer" style="top:285px;height:53px;background:var(--navy)">
    <div class="layer__item" style="left:16px;top:14px"><span class="dot" style="border-radius:2px;background:none;border:1px solid #fff"></span>Software<br>Defined Network</div>
    <div class="layer__item" style="left:112px;top:14px"><span class="dot" style="border-radius:2px;background:none;border:1px solid #fff"></span>DC<br>Inter-connect</div>
    <div class="layer__item" style="left:198px;top:18px"><span class="dot"></span>IP comms</div>
  </div>
  <div class="layer" style="top:338px;height:42px;background:var(--grey)">
    <div class="layer__item" style="left:20px;top:9px"><span class="dot" style="background:none"></span>IP/MPLS<br>Edge &amp; Core</div>
    <div class="layer__item" style="left:150px;top:5px"><span class="dot" style="background:none"></span>IoT<br>Optimized<br>Core</div>
  </div>
  <div class="layer" style="top:380px;height:46px;background:var(--dark)">
    <div class="layer__item" style="left:16px;top:13px">Mobile &amp; Fixed Access IP Backhaul<br>Small Cells/WLAN/LPWAN</div>
  </div>

  <div class="tag" style="top:216px;background:var(--dark)">City Application</div>
  <div class="tag" style="top:243px;background:var(--sky)">City IoT platform</div>
  <div class="tag" style="top:300px;background:var(--navy)">City cloud</div>
  <div class="tag" style="top:346px;background:var(--grey)">City -wide access</div>
  <div class="tag" style="top:392px;background:var(--dark)">City devices &amp; sensors</div>

  <h2 class="subhead" style="top:470px;font-size:14px">How we help you get the most from your IoT and M2M solutions</h2>
  <p class="copy" style="left:22px;top:496px;width:492px">We are committed to delivering connected solutions that transform business productivity. We believe that IoT technology is changing the way businesses operate helping to drive operational efficiency, customer experience improvements and enabling new service-based revenue streams.</p>
  <h3 class="subhead" style="top:547px;font-size:12px">Our commitment Is demonstrated through:</h3>
  <ol class="commit">
    <li><b>1</b><span>Australia's largest mobile network, including the addition of Narrowband-IoT providing greater coverage and a range of connectivity options to you.</span></li>
    <li><b>2</b><span>Ongoing investment in services, platforms and partners to enable innovative IoT solutions.</span></li>
    <li><b>3</b><span>Continued focus on helping businesses across all industries to understand and adopt IoT technology.</span></li>
    <li><b>4</b><span>Our uncompromising dedication to customer service.</span></li>
    <li><b>5</b><span>Our ability to deliver innovative end-to-end IoT solutions.</span></li>
  </ol>
</section>

</body>
</html>
```